Dentist Seminar invite please see .doc in attachments

Need an 8.5 x 11 invite designed. It will be for an invitation to attend an evening seminar on dental procedures. Feel free to utilize both front and back ONLY IF REQUIRED

See Assets & PPT with additional assets.

INSPIRATION: FIle NAME KOLVEN

Target Market(s)

Dentists

Industry/Entity Type

Dental

Other font styles liked:
• lato, garamond, palatino linotype

Colors
cee9f5
9bcb3c
0492cd
cadf82

Requirements
Must have
• Must have the colours suggested, and professional feel.
• Some of the assets merged cleanly into the design
Should not have
• Any pictures of teeth, tooth brushes or any dental product

```html
<!DOCTYPE html>
<html lang="en">
<head>
<meta charset="utf-8">
<title>Dental Seminar Invitation</title>
<link href="https://fonts.googleapis.com/css2?family=Montserrat:wght@400;500;600;700;800&display=swap" rel="stylesheet">
<style>
  :root{
    --blue:#1f5ea8;
    --navy:#1c2240;
    --green:#8dc63f;
    --ink:#2b2b2b;
    --white:#ffffff;
  }
  *{box-sizing:border-box;margin:0;padding:0}
  html,body{width:842px;height:1200px;overflow:hidden;background:var(--white)}
  body{font-family:"Montserrat",sans-serif;color:var(--ink)}
  .flyer{position:relative;width:842px;height:1200px;overflow:hidden;background:var(--white)}

  .hero-fade{position:absolute;left:0;top:0;width:420px;height:600px;
    background:linear-gradient(180deg,#ffffff 0%,#eef0f2 100%)}
  .hero-photo{position:absolute;right:0;top:0;width:520px;height:600px;
    background:linear-gradient(90deg,rgba(255,255,255,1) 0%,rgba(220,226,232,.6) 22%,rgba(58,86,120,.85) 55%,#2b4566 100%),
               linear-gradient(180deg,#8fa3b8 0%,#3c5a7d 60%,#1f3550 100%);}

  .headline{position:absolute;left:36px;top:48px;line-height:1.02;text-transform:uppercase}
  .headline .light{display:block;color:var(--blue);font-weight:500;font-size:58px;letter-spacing:.5px}
  .headline .bold{display:block;color:var(--green);font-weight:800;font-size:64px}

  .swoosh{position:absolute;left:0;top:0;width:842px;height:1200px;pointer-events:none}

  .objectives{position:absolute;left:44px;top:636px;width:410px}
  .section-title{font-size:29px;color:var(--blue);font-weight:400}
  .section-title strong{color:var(--green);font-weight:700}
  .title-rule{width:60px;height:2px;background:var(--blue);margin:4px 0 22px}
  .objective-list{list-style:none}
  .objective-list li{position:relative;padding-left:24px;font-size:15.5px;line-height:1.32;margin-bottom:14px;color:var(--ink)}
  .objective-list li svg{position:absolute;left:0;top:4px;width:14px;height:14px}

  .bio-panel{position:absolute;left:470px;top:604px;width:372px;height:516px;background:var(--blue);padding:26px 24px 0 26px}
  .bio-title{color:var(--green);font-size:28px;font-weight:700;line-height:1.2}
  .bio-rule{width:34px;height:2px;background:var(--white);margin:8px 0 12px}
  .bio-text{color:var(--white);font-size:14.5px;line-height:1.4}

  .event-box{position:absolute;left:494px;top:864px;width:322px;height:246px;background:var(--green);border-radius:4px;
    color:var(--white);padding:12px 18px 0;text-align:center}
  .date-row{display:flex;justify-content:center;align-items:stretch;gap:6px}
  .date-main{display:flex;flex-direction:column;align-items:flex-start}
  .month{font-size:32px;font-weight:800;line-height:1}
  .day{font-size:88px;font-weight:800;line-height:.86;letter-spacing:-3px}
  .year{writing-mode:vertical-rl;font-size:28px;font-weight:800;line-height:1;letter-spacing:1px}
  .time{display:flex;align-items:center;justify-content:center;gap:10px;color:var(--navy);font-size:27px;font-weight:500;margin-top:6px;line-height:1.2}
  .venue{margin-top:6px;font-size:13px;font-weight:600;line-height:1.28}
  .venue svg{display:block;margin:0 auto 3px}

  .footer{position:absolute;left:0;top:1120px;width:842px;height:66px;background:var(--navy);
    display:flex;align-items:center;justify-content:center;gap:22px;color:var(--white);font-size:20px;font-weight:600}
  .footer .item{display:flex;align-items:center;gap:10px}
  .footer .divider{width:1px;height:34px;background:rgba(255,255,255,.6)}
  .footer-stripe{position:absolute;left:0;top:1186px;width:842px;height:14px;background:linear-gradient(90deg,var(--green) 0 72%,var(--blue) 72% 100%)}
</style>
</head>
<body>
<main class="flyer">
  <div class="hero-fade"></div>
  <div class="hero-photo" role="img" aria-label="Photo of a smiling family of four sitting in an open convertible car, seen from above"></div>

  <h1 class="headline">
    <span class="light">Lorem</span>
    <span class="light">Ipsum is</span>
    <span class="bold">Simply</span>
    <span class="bold">Dummy</span>
    <span class="bold">Text</span>
  </h1>

  <svg class="swoosh" viewBox="0 0 842 1200" aria-hidden="true">
    <path d="M0 470 C150 545 420 585 842 575 L842 620 L0 620 Z" fill="var(--white)"/>
    <path d="M0 420 C150 515 420 565 842 552 L842 572 C420 588 150 545 0 452 Z" fill="var(--blue)"/>
    <path d="M0 470 C70 520 150 552 240 572 C140 585 60 600 0 620 Z" fill="var(--green)"/>
    <path d="M0 610 C250 575 550 570 842 588 L842 606 C550 590 250 598 0 624 Z" fill="var(--navy)"/>
  </svg>

  <section class="objectives">
    <h2 class="section-title">Learning <strong>Objectives</strong></h2>
    <div class="title-rule"></div>
    <ul class="objective-list">
      <li><svg viewBox="0 0 14 14"><circle cx="7" cy="7" r="7" fill="var(--green)"/><path d="M4 7h5M7 4.5 9.5 7 7 9.5" stroke="#fff" stroke-width="1.6" fill="none"/></svg>Discuss the use of modern digital technologies like CBCT, intra-oral scanning, and 3D printing.</li>
      <li><svg viewBox="0 0 14 14"><circle cx="7" cy="7" r="7" fill="var(--green)"/><path d="M4 7h5M7 4.5 9.5 7 7 9.5" stroke="#fff" stroke-width="1.6" fill="none"/></svg>Learn to digitally plan surgical procedures and use 3D printed surgical guides</li>
      <li><svg viewBox="0 0 14 14"><circle cx="7" cy="7" r="7" fill="var(--green)"/><path d="M4 7h5M7 4.5 9.5 7 7 9.5" stroke="#fff" stroke-width="1.6" fill="none"/></svg>Understand the benefits of microsurgery and the use of surgical operating microscope</li>
      <li><svg viewBox="0 0 14 14"><circle cx="7" cy="7" r="7" fill="var(--green)"/><path d="M4 7h5M7 4.5 9.5 7 7 9.5" stroke="#fff" stroke-width="1.6" fill="none"/></svg>Understand the benefits of digital technology in surgical treatment planning</li>
      <li><svg viewBox="0 0 14 14"><circle cx="7" cy="7" r="7" fill="var(--green)"/><path d="M4 7h5M7 4.5 9.5 7 7 9.5" stroke="#fff" stroke-width="1.6" fill="none"/></svg>Understanding and benefits of live guided navigation surgery and its applications</li>
      <li><svg viewBox="0 0 14 14"><circle cx="7" cy="7" r="7" fill="var(--green)"/><path d="M4 7h5M7 4.5 9.5 7 7 9.5" stroke="#fff" stroke-width="1.6" fill="none"/></svg>Learn about innovative procedures like digitally guided bone block harvesting, digitally created bone grafts, and osteotomy guides.</li>
      <li><svg viewBox="0 0 14 14"><circle cx="7" cy="7" r="7" fill="var(--green)"/><path d="M4 7h5M7 4.5 9.5 7 7 9.5" stroke="#fff" stroke-width="1.6" fill="none"/></svg>Understand how computer automated design software can improve upon real live surgery</li>
    </ul>
  </section>

  <section class="bio-panel">
    <h2 class="bio-title">Biography</h2>
    <div class="bio-rule"></div>
    <p class="bio-text">Lorem Ipsum is simply dummy text of the printing and typesetting industry. Lorem Ipsum has been the industry's standard dummy text ever since the 1500s, when an unknown printer took a galley of type and scrambled it to make a type specimen book.</p>
  </section>

  <section class="event-box">
    <div class="date-row">
      <div class="date-main">
        <span class="month">NOVEMBER</span>
        <span class="day">13TH</span>
      </div>
      <span class="year">2017</span>
    </div>
    <div class="time">
      <svg width="28" height="28" viewBox="0 0 30 30" aria-hidden="true"><circle cx="15" cy="15" r="13" fill="none" stroke="#fff" stroke-width="2"/><path d="M15 7v8h6" stroke="#fff" stroke-width="2" fill="none"/></svg>
      6:30 – 9:30PM
    </div>
    <div class="venue">
      <svg width="16" height="20" viewBox="0 0 18 22" aria-hidden="true"><path d="M9 1C4.6 1 1.5 4.2 1.5 8.3 1.5 13.5 9 21 9 21s7.5-7.5 7.5-12.7C16.5 4.2 13.4 1 9 1z" fill="none" stroke="#fff" stroke-width="1.8"/><circle cx="9" cy="8.3" r="2.6" fill="none" stroke="#fff" stroke-width="1.6"/></svg>
      Maple Hall Event Centre<br>480 Harlow St. Toronto,<br>Ontario M4B 1K7
    </div>
  </section>

  <footer class="footer">
    <span class="item">
      <svg width="20" height="20" viewBox="0 0 24 24" aria-hidden="true"><path d="M6.6 10.8a15.1 15.1 0 0 0 6.6 6.6l2.2-2.2c.3-.3.7-.4 1-.2 1.1.4 2.3.6 3.6.6.6 0 1 .4 1 1V20c0 .6-.4 1-1 1A17 17 0 0 1 3 4c0-.6.4-1 1-1h3.5c.6 0 1 .4 1 1 0 1.3.2 2.5.6 3.6.1.3 0 .7-.2 1z" fill="#fff"/></svg>
      416-555-0148
    </span>
    <span class="divider"></span>
    <span class="item">
      <svg width="22" height="16" viewBox="0 0 22 16" aria-hidden="true"><rect x="1" y="1" width="20" height="14" fill="none" stroke="#fff" stroke-width="1.6"/><path d="M1 1l10 8 10-8" fill="none" stroke="#fff" stroke-width="1.6"/></svg>
      kolven.desk@mailbox.com
    </span>
  </footer>
  <div class="footer-stripe"></div>
</main>
</body>
</html>
```